Business Card Design - R.T. Custom Cabinets Ltd.

Design a business card, including a new logo for a new company in Vancouver, British Columbia, Canada.

The logo must be available as a separate file.

The card should include all company information including:
R.T. Custom Cabinets Ltd.
2786 Larchmoor Crescent
Burnaby, B.C. V7K 2P9
Telehone: 604-XXX-XXXX
Fax: 604-XXX-XXXX
www.rtcustomcabinets.example

As well as individual contact information for employees:
Name
Position
Telephone
Email

The card must include a thoughtful message as well

Target Market(s)

Custom Cabinets

Industry/Entity Type

Business

Contact Information for Business Card

Important information on the front, thoughtful message on the back

Colors
fbed22
9bcb3c
0355a3
ec1f27

Requirements
Must have
• See project description
Nice to have
• images that showcase custom cabinets (european, modern and traditional) styles

```html
<!DOCTYPE html>
<html lang="en">
<head>
<meta charset="utf-8">
<title>R.T. Custom Cabinets – Business Card</title>
<link rel="stylesheet" href="https://fonts.googleapis.com/css2?family=Source+Sans+3:ital,wght@0,400;0,600;0,700;1,400&display=swap">
<style>
  :root {
    --stage: #3b2818;
    --card: #f7f7f6;
    --ink: #2a1a10;
    --grey: #5f5f5f;
    --yellow: #fbed22;
    --green: #9bcb3c;
    --blue: #0355a3;
    --red: #ec1f27;
  }
  * { margin: 0; padding: 0; box-sizing: border-box; }
  html, body { width: 1200px; height: 799px; overflow: hidden; }
  body {
    background: var(--stage);
    font-family: "Source Sans 3", "Myriad Pro", Arial, sans-serif;
    position: relative;
  }
  .card {
    position: absolute;
    width: 530px;
    height: 303px;
    background: var(--card);
    border-radius: 26px;
    overflow: hidden;
    box-shadow: 0 14px 30px rgba(0,0,0,.45);
  }
  .colour-band {
    position: absolute; left: 0; right: 0; bottom: 0; height: 22px;
    display: flex;
  }
  .colour-band span { flex: 1; }
  .colour-band .c-yellow { background: var(--yellow); }
  .colour-band .c-green { background: var(--green); }
  .colour-band .c-blue { background: var(--blue); }
  .colour-band .c-red { background: var(--red); }

  .brand-square { width: 22px; height: 22px; background: var(--red); flex: none; }
  .brand-name { font-weight: 700; color: var(--blue); line-height: 1; }

  /* Back of card */
  .card-back { left: 60px; top: 90px; }
  .card-back .brand {
    position: absolute; left: 0; right: 0; top: 52px;
    display: flex; align-items: center; justify-content: center; gap: 10px;
  }
  .card-back .brand-name { font-size: 30px; }
  .services {
    position: absolute; left: 0; right: 0; top: 110px;
    text-align: center; color: var(--grey); font-size: 15px; line-height: 1.3;
  }
  .services .dash { color: var(--red); margin: 0 8px; font-weight: 700; }
  .message {
    position: absolute; left: 50px; right: 50px; top: 172px;
    text-align: center; font-size: 15px; font-style: italic; color: var(--green);
    line-height: 1.3;
  }
  .back-web {
    position: absolute; left: 0; right: 0; top: 236px;
    text-align: center; font-size: 14px; letter-spacing: 2px; color: var(--grey);
  }
  .back-web .site { color: var(--blue); }

  /* Front of card */
  .card-front { left: 610px; top: 400px; }
  .wordmark {
    position: absolute; left: 32px; top: 52px;
    display: flex; align-items: flex-start; gap: 10px;
  }
  .wordmark .brand-square { margin-top: 6px; }
  .wordmark .brand-name { font-size: 34px; line-height: .95; }
  .person { position: absolute; left: 300px; top: 36px; }
  .person-name { font-size: 19px; font-weight: 700; color: var(--red); line-height: 1.1; }
  .person-role { font-size: 13px; color: var(--grey); }
  .contact {
    position: absolute; left: 270px; top: 118px; list-style: none;
    font-size: 13px; color: var(--grey); line-height: 18px;
  }
  .contact li { display: flex; align-items: center; gap: 6px; white-space: nowrap; }
  .contact .plain { padding-left: 20px; }
  .icon { width: 14px; height: 14px; flex: none; }
</style>
</head>
<body>

<section class="card card-back" aria-label="Card back">
  <div class="brand">
    <span class="brand-square"></span>
    <span class="brand-name">R.T. Custom Cabinets</span>
  </div>
  <p class="services">
    Kitchens<span class="dash">-</span>Bathrooms<span class="dash">-</span>Offices / Libraries<br>
    Custom Wine / Spirits Storage
  </p>
  <p class="message">Crafted with care, built to last &mdash; cabinets made for the way you live.</p>
  <p class="back-web">- www.<span class="site">rtcustomcabinets</span>.example -</p>
  <div class="colour-band"><span class="c-yellow"></span><span class="c-green"></span><span class="c-blue"></span><span class="c-red"></span></div>
</section>

<section class="card card-front" aria-label="Card front">
  <div class="wordmark">
    <span class="brand-square"></span>
    <span class="brand-name">R.T.<br>Custom<br>Cabinets</span>
  </div>

  <div class="person">
    <p class="person-name">Daniel Marchetti</p>
    <p class="person-role">Business Manager</p>
  </div>

  <ul class="contact">
    <li class="plain">2786 Larchmoor Crescent</li>
    <li class="plain">Burnaby, B.C. V7K 2P9</li>
    <li>
      <svg class="icon" viewBox="0 0 14 14" aria-hidden="true"><circle cx="7" cy="7" r="7" fill="#0355a3"/><path d="M4.5 3.5h1.5l.7 2-1 .8a5 5 0 0 0 2 2l.8-1 2 .7V9.5a1 1 0 0 1-1 1A6 6 0 0 1 3.5 4.5a1 1 0 0 1 1-1z" fill="#fff"/></svg>
      Tel (604) 555-0143
    </li>
    <li>
      <svg class="icon" viewBox="0 0 14 14" aria-hidden="true"><circle cx="7" cy="7" r="7" fill="#0355a3"/><rect x="4" y="3" width="6" height="3" fill="#fff"/><rect x="3" y="6" width="8" height="3.5" fill="#fff"/><rect x="4.5" y="8.5" width="5" height="2.5" fill="#fff" stroke="#0355a3" stroke-width=".6"/></svg>
      Fax 604-XXX-XXXX
    </li>
    <li>
      <svg class="icon" viewBox="0 0 14 14" aria-hidden="true"><circle cx="7" cy="7" r="7" fill="#0355a3"/><rect x="5" y="3" width="4" height="8" rx="1" fill="#fff"/></svg>
      Cell 604-XXX-XXX2
    </li>
    <li>
      <svg class="icon" viewBox="0 0 14 14" aria-hidden="true"><circle cx="7" cy="7" r="7" fill="#0355a3"/><rect x="3.5" y="4.5" width="7" height="5" fill="#fff"/><path d="M3.5 4.5 7 7.5l3.5-3" fill="none" stroke="#0355a3" stroke-width=".8"/></svg>
      daniel@rtcustomcabinets.example
    </li>
    <li>
      <svg class="icon" viewBox="0 0 14 14" aria-hidden="true"><circle cx="7" cy="7" r="7" fill="#0355a3"/><circle cx="7" cy="7" r="3.8" fill="none" stroke="#fff" stroke-width=".9"/><path d="M3.2 7h7.6M7 3.2v7.6" stroke="#fff" stroke-width=".8"/></svg>
      www.rtcustomcabinets.example
    </li>
  </ul>
  <div class="colour-band"><span class="c-yellow"></span><span class="c-green"></span><span class="c-blue"></span><span class="c-red"></span></div>
</section>

</body>
</html>
```